Bright Path Therapies business cards and stationary

Need business cards and stationary designed to match previously made logo for for a new company based in Sydney NSW called 'Bright Path Therapies'.

We provide early intervention services and diagnostic assessment for children with disability and their families. I would like designs that are colourful and child friendly - possibly using feet/footprints/steps on a white background. The final design should communicate that we are family friendly, accepting and fun to work with.

Target Market(s)

Parents and Families
Teachers
Allied Health Professionals

Industry/Entity Type

Psychology

Contact Information for Business Card

Bright Path Therapies
www.brightpaththerapies.example
info@brightpaththerapies.example

Font styles to use
Sans Serif
Decorative
Script

Requirements
Must have
• Match the font and colour scheme of logo, along with footprint picture
Nice to have
• Clean and simple, while reflecting that I am working with families.
• Also- editable for when we make staff specific cards.

```html
<!DOCTYPE html>
<html lang="en">
<head>
<meta charset="utf-8">
<title>Bright Path Therapies – Business Cards</title>
<link rel="stylesheet" href="https://fonts.googleapis.com/css2?family=Josefin+Sans:wght@400&family=Arimo:wght@400;700&display=swap">
<style>
  :root {
    --bg: #d9d9dc;
    --card: #ffffff;
    --navy: #14146b;
    --sky: #8fb7e3;
    --brand-blue: #1f7bc1;
    --red: #ef4136;
    --orange: #f7941d;
    --green: #8dc63f;
    --yellow: #ffd200;
  }
  * { box-sizing: border-box; margin: 0; padding: 0; }
  html, body { width: 1199px; height: 1200px; overflow: hidden; }
  body {
    background: linear-gradient(160deg, #f1f1f2 0%, var(--bg) 100%);
    font-family: "Arimo", Arial, sans-serif;
    position: relative;
  }
  .card {
    position: absolute;
    left: 150px;
    width: 900px;
    height: 514px;
    background: var(--card);
    box-shadow: 0 14px 30px rgba(0,0,0,0.18);
    overflow: hidden;
  }
  .card--front { top: 60px; }
  .card--back { top: 626px; }

  .footprint-trail {
    position: absolute;
    width: 70px;
    border-radius: 35px;
    background: linear-gradient(180deg, var(--yellow) 0%, var(--green) 22%, var(--orange) 45%, var(--red) 65%, var(--yellow) 82%, var(--green) 100%);
    opacity: 0.55;
    transform-origin: top center;
  }
  .card--front .footprint-trail { left: 40px; top: -20px; height: 600px; transform: rotate(-24deg); }
  .card--back .footprint-trail { left: 110px; top: -20px; height: 620px; transform: rotate(-22deg); }

  .brand {
    position: absolute;
    left: 300px;
    top: 210px;
    display: flex;
    align-items: center;
    gap: 22px;
  }
  .brand__dot {
    width: 92px; height: 92px;
    border-radius: 50%;
    background: var(--red);
    flex: none;
  }
  .brand__name {
    font-family: "Josefin Sans", "Trebuchet MS", sans-serif;
    font-weight: 400;
    font-size: 46px;
    color: var(--brand-blue);
    letter-spacing: 1px;
  }

  .person {
    position: absolute;
    left: 520px;
    top: 92px;
    text-align: center;
    width: 260px;
  }
  .person__name { font-weight: 700; font-size: 26px; color: var(--navy); }
  .person__title { font-weight: 700; font-size: 24px; color: var(--sky); margin-top: 2px; }

  .contacts {
    position: absolute;
    left: 480px;
    top: 230px;
    list-style: none;
  }
  .contacts__item {
    display: flex;
    align-items: center;
    gap: 16px;
    font-size: 17px;
    color: var(--navy);
    margin-bottom: 18px;
  }
  .contacts__icon { width: 36px; height: 36px; flex: none; }
</style>
</head>
<body>
  <section class="card card--front">
    <div class="footprint-trail" role="img" aria-label="Trail of colourful footprints"></div>
    <div class="brand">
      <span class="brand__dot"></span>
      <span class="brand__name">Bright Path Therapies</span>
    </div>
  </section>

  <section class="card card--back">
    <div class="footprint-trail" role="img" aria-label="Trail of colourful footprints"></div>
    <div class="person">
      <div class="person__name">YOUR NAME</div>
      <div class="person__title">job title</div>
    </div>
    <ul class="contacts">
      <li class="contacts__item">
        <svg class="contacts__icon" viewBox="0 0 36 36"><circle cx="18" cy="18" r="18" fill="#8fb7e3"/><path d="M18 8a7 7 0 0 0-7 7c0 5 7 13 7 13s7-8 7-13a7 7 0 0 0-7-7z" fill="#fff"/><circle cx="18" cy="15" r="2.6" fill="#8fb7e3"/></svg>
        Company address
      </li>
      <li class="contacts__item">
        <svg class="contacts__icon" viewBox="0 0 36 36"><circle cx="18" cy="18" r="18" fill="#8fb7e3"/><path d="M12 9c1.5-.5 2.5 2 3.5 4 .6 1.2-1.2 2-1 3 .6 2 2.5 4 4.5 4.8 1 .3 1.8-1.6 3-1 2 1 4.5 2 4 3.5-.8 2.4-3 3.2-5 2.6C15.5 24.4 11.5 20 10 14.5c-.5-2.2.3-4.8 2-5.5z" fill="#fff"/></svg>
        Phone of the company
      </li>
      <li class="contacts__item">
        <svg class="contacts__icon" viewBox="0 0 36 36"><circle cx="18" cy="18" r="18" fill="#8fb7e3"/><rect x="9" y="12" width="18" height="12" fill="none" stroke="#fff" stroke-width="1.8"/><path d="M9 12l9 7 9-7M9 24l6.5-6M27 24l-6.5-6" fill="none" stroke="#fff" stroke-width="1.5"/></svg>
        info@brightpaththerapies.example
      </li>
      <li class="contacts__item">
        <svg class="contacts__icon" viewBox="0 0 36 36"><circle cx="18" cy="18" r="18" fill="#8fb7e3"/><circle cx="18" cy="18" r="10" fill="none" stroke="#fff" stroke-width="1.6"/><ellipse cx="18" cy="18" rx="4.5" ry="10" fill="none" stroke="#fff" stroke-width="1.4"/><path d="M8 18h20" stroke="#fff" stroke-width="1.4"/></svg>
        www.brightpaththerapies.example
      </li>
    </ul>
  </section>
</body>
</html>
```